its a new company based in Christchurch new Zealand building computers ,repairs, upgrades and anything computers for the general public,i like bright happy colours like yellows, greens reds anything that stands out and it needs to communicant trust and security towards my new company,i have no logo yet,

Target Market(s)

target market of all ages

Industry/Entity Type

Building

Contact Information for Business Card

Pixel Harbour Limited,ph-0214862735,email-bluefoxtrail17@mailnest.example,4c marlowe rd,fernvale

```html
<!DOCTYPE html>
<html lang="en">
<head>
<meta charset="utf-8">
<title>Pixel Harbour Limited – Business Card</title>
<link rel="stylesheet" href="https://fonts.googleapis.com/css2?family=Exo+2:wght@400;600;700&display=swap">
<style>
  :root {
    --page-bg: #e9ecf1;
    --card-white: #ffffff;
    --sky-blue: #22a6e2;
    --sky-blue-light: #6cc6ef;
    --steel-blue: #5a78b6;
    --text-light: #ffffff;
  }
  * { margin: 0; padding: 0; box-sizing: border-box; }
  html, body {
    width: 1200px;
    height: 901px;
    overflow: hidden;
    background: var(--page-bg);
    font-family: "Exo 2", sans-serif;
  }
  .stage {
    width: 1200px;
    height: 901px;
    display: flex;
    align-items: center;
    justify-content: center;
  }
  .business-card {
    position: relative;
    width: 1000px;
    height: 580px;
    background: var(--card-white);
    border-radius: 48px;
    overflow: hidden;
    box-shadow: 0 18px 40px rgba(40, 60, 100, 0.18);
  }
  .card-waves {
    position: absolute;
    inset: 0;
    width: 100%;
    height: 100%;
  }
  .brand {
    position: absolute;
    left: 170px;
    top: 78px;
    display: flex;
    align-items: center;
    gap: 14px;
  }
  .brand-dot {
    width: 30px;
    height: 30px;
    border-radius: 50%;
    background: var(--sky-blue);
  }
  .brand-name {
    font-weight: 700;
    font-size: 34px;
    color: var(--steel-blue);
    letter-spacing: 0.5px;
  }
  .holder {
    position: absolute;
    left: 200px;
    top: 180px;
    color: var(--sky-blue);
  }
  .holder-name {
    font-weight: 600;
    font-size: 36px;
    letter-spacing: 1.5px;
    text-transform: uppercase;
  }
  .holder-role {
    font-weight: 400;
    font-size: 24px;
    margin-top: 4px;
  }
  .contact-list {
    position: absolute;
    left: 500px;
    top: 405px;
    list-style: none;
    color: var(--text-light);
    font-size: 20px;
  }
  .contact-item {
    display: flex;
    align-items: center;
    gap: 12px;
    height: 32px;
  }
  .contact-icon {
    width: 22px;
    height: 22px;
    flex: none;
  }
</style>
</head>
<body>
<main class="stage">
  <section class="business-card">
    <svg class="card-waves" viewBox="0 0 1000 580" preserveAspectRatio="none" aria-hidden="true">
      <defs>
        <linearGradient id="steelFill" x1="0" y1="0" x2="1" y2="1">
          <stop offset="0" stop-color="#5471b0"/>
          <stop offset="0.5" stop-color="#7392cf"/>
          <stop offset="1" stop-color="#5a78b6"/>
        </linearGradient>
      </defs>
      <path d="M95,150 C108,230 160,282 240,312" fill="none" stroke="var(--sky-blue-light)" stroke-width="6" stroke-linecap="round"/>
      <path d="M0,290 C140,350 380,370 620,315 C800,272 920,275 1000,300 L1000,365 C880,335 760,335 600,372 C380,420 150,412 0,350 Z" fill="var(--sky-blue)"/>
      <path d="M0,350 C150,412 380,420 600,372 C760,335 880,335 1000,365" fill="none" stroke="#ffffff" stroke-width="8"/>
      <path d="M0,366 C150,428 380,436 600,388 C770,350 900,355 1000,385 L1000,580 L0,580 Z" fill="url(#steelFill)"/>
      <path d="M680,380 C800,360 920,368 1000,390 L1000,440 C950,415 850,395 680,386 Z" fill="var(--sky-blue)"/>
      <path d="M700,392 C850,400 950,425 1000,455" fill="none" stroke="#ffffff" stroke-width="6"/>
    </svg>

    <div class="brand">
      <span class="brand-dot"></span>
      <span class="brand-name">Pixel Harbour Limited</span>
    </div>

    <div class="holder">
      <p class="holder-name">Nina Walsh</p>
      <p class="holder-role">Managing Director</p>
    </div>

    <ul class="contact-list">
      <li class="contact-item">
        <svg class="contact-icon" viewBox="0 0 24 24" aria-hidden="true"><circle cx="12" cy="12" r="12" fill="#fff"/><path d="M9 6h2l1 3-1.5 1a6 6 0 0 0 3.5 3.5l1-1.5 3 1v2a2 2 0 0 1-2 2A10 10 0 0 1 7 8a2 2 0 0 1 2-2z" fill="#5a78b6"/></svg>
        <span>0214862735</span>
      </li>
      <li class="contact-item">
        <svg class="contact-icon" viewBox="0 0 24 24" aria-hidden="true"><circle cx="12" cy="12" r="12" fill="#fff"/><path d="M9 6h2l1 3-1.5 1a6 6 0 0 0 3.5 3.5l1-1.5 3 1v2a2 2 0 0 1-2 2A10 10 0 0 1 7 8a2 2 0 0 1 2-2z" fill="#5a78b6"/></svg>
        <span>0214862735</span>
      </li>
      <li class="contact-item">
        <svg class="contact-icon" viewBox="0 0 24 24" aria-hidden="true"><circle cx="12" cy="12" r="12" fill="#fff"/><rect x="6" y="8" width="12" height="8" rx="1" fill="#5a78b6"/><path d="M6 8l6 5 6-5" fill="none" stroke="#fff" stroke-width="1.2"/></svg>
        <span>bluefoxtrail17@mailnest.example</span>
      </li>
      <li class="contact-item">
        <svg class="contact-icon" viewBox="0 0 24 24" aria-hidden="true"><circle cx="12" cy="12" r="12" fill="#fff"/><circle cx="12" cy="12" r="6.5" fill="none" stroke="#5a78b6" stroke-width="1.5"/><path d="M5.5 12h13M12 5.5c-3 3.5-3 9.5 0 13M12 5.5c3 3.5 3 9.5 0 13" fill="none" stroke="#5a78b6" stroke-width="1.2"/></svg>
        <span>www.pixelharbour.example</span>
      </li>
      <li class="contact-item">
        <svg class="contact-icon" viewBox="0 0 24 24" aria-hidden="true"><circle cx="12" cy="12" r="12" fill="#fff"/><path d="M12 5a4.5 4.5 0 0 1 4.5 4.5C16.5 13 12 19 12 19S7.5 13 7.5 9.5A4.5 4.5 0 0 1 12 5z" fill="#5a78b6"/><circle cx="12" cy="9.5" r="1.7" fill="#fff"/></svg>
        <span>4c marlowe rd, fernvale</span>
      </li>
    </ul>
  </section>
</main>
</body>
</html>
```